TapDelver Rex (TVDR) – Official Website & Presale Landing Page

TapDelver Rex (TVDR) is a meme-inspired crypto project built on Veltora, designed to allow users to mine tokens directly from their mobile phones. Our mission is to bring crypto mining to everyone in a simple, fun, and viral way – powered by community engagement, humor, and innovation.

The project combines the simplicity of mobile mining with the viral potential of meme culture. Unlike traditional mining, TapDelver Rex does not require expensive equipment or complex setups. Instead, users participate directly from their smartphones, making the project accessible to millions of young investors worldwide.

The landing page will be the central hub for our community. It must be modern, responsive, and visually striking. Key sections should include: Hero section with call-to-action, Tokenomics, Roadmap, Miner Counter ("12,438 Miners and Counting"), Airdrop countdown, App preview, Social media links (Chatwire, Q/Blurbly, Corvid Wallet), and Contact information. We also want a dedicated section for Presale where investors can join directly once the presale goes live.

Nice-to-have features include animated counters, interactive roadmap, video embedding, newsletter signup, global map of miners, dark mode toggle, and a multilingual setup (English, Vietnamese, Chinese, French, German, Slovak). The style should be futuristic, colorful, and engaging – with neon tones and crypto/meme vibes.

The target market is young crypto investors, meme communities, and global users looking for new opportunities in Web3. Our ultimate goal is to grow rapidly, build strong hype, and raise $7M+ during the presale.

The website should reflect excitement, simplicity, and trustworthiness while staying true to meme culture. It must balance professional design with playful elements, creating an experience that keeps users engaged and excited to be part of TapDelver Rex.

Target Market(s)

Young crypto investors, meme community, people interested in mobile mining (18–35 years).

Industry/Entity Type

Cryptocurrency / Blockchain / Technology

Coding

Coded - Design and coding required

Number of Pages Required

5+ page

Font styles to use
Sans Serif

Colors
A7469A
B969AE
D3A5CF
EDDBEB
F8F0F9
6B429C
8869AF
B7A5CE
E3DAEB
F3F0F8

Requirements
Must have
• Must Haves: - Responsive landing page with sections: Hero (headline, subheadline, CTA button), Tokenomics, Total Supply, Roadmap, Airdrop, App, Team/Founder, Contact, Social links (X, Chatwire, Email). - Additional dedicated Presale Landing Page (1 page) with: - Hero headline (Join the $TVDR Presale – Mine Crypto From Your Phone!) + CTA button (Buy TVDR Now). - Countdown timer for presale phase. - Presale phases (3 phases) with price and allocation: - Phase 1 – Private Sale: $0.005, 100M TVDR - Phase 2 – Public Sale: $0.01, 150M TVDR - Phase 3 – Final Sale: $0.02, 100M TVDR - Total presale allocation: 350M TVDR (35% of supply). - “How to Participate” steps (Connect wallet → Select amount → Confirm transaction → Claim tokens). - Claim system placeholder (button). - Security & trust badges: verified contract on Ledgrix, transparent tokenomics, locked liquidity. - Fully modern, clean, crypto-style design with bold colors (purple + dark + neon contrasts). - Clear CTA buttons (Buy, Join Airdrop, Connect Wallet). - Mobile-friendly (responsive) design.
Nice to have
• Animated counters (e.g., "12,438 Miners and Counting"). - Interactive roadmap with hover/scroll reveal. - Language switcher (at least 5–7 languages: English, Vietnamese, Chinese, French, German, Slovak). - Embedded promo video (ClipVault/Reelio). - Newsletter signup (email capture / Postorca). - Global miners map (optional). - Countdown timers for presale and airdrop. - Light parallax/particle background (neon/futuristic). - Dark mode toggle (optional). - Simple CMS-friendly structure (easy to add blog/updates later).
Should not have
• Too formal corporate style, long boring text, outdated templates.

```html
<!DOCTYPE html>
<html lang="en">
<head>
<meta charset="utf-8">
<title>TapDelver Rex (TVDR) – Mine Crypto Anywhere</title>
<link href="https://fonts.googleapis.com/css2?family=Outfit:wght@400;500;600;700&family=Poppins:wght@400;500;600;700&display=swap" rel="stylesheet">
<style>
:root{
  --bg-deep:#13072a;
  --violet:#6b429c;
  --violet-soft:#8869af;
  --lilac:#b7a5ce;
  --orchid:#a7469a;
  --btn-start:#e07ae0;
  --btn-end:#8d55e6;
  --num:#b06cf0;
  --white:#ffffff;
  --muted:#c9bfd9;
  --line:rgba(255,255,255,.14);
}
*{box-sizing:border-box;margin:0;padding:0}
html,body{width:1200px;height:1140px;overflow:hidden}
body{
  font-family:"Outfit",sans-serif;color:var(--white);
  background:
    radial-gradient(600px 420px at 900px 60px,rgba(167,70,154,.45),transparent 70%),
    radial-gradient(500px 500px at 1180px 600px,rgba(167,70,154,.35),transparent 70%),
    radial-gradient(700px 500px at 200px 900px,rgba(107,66,156,.25),transparent 70%),
    linear-gradient(180deg,#1d0b3a 0%,var(--bg-deep) 60%,#1a0834 100%);
}
.page{position:relative;width:1200px;height:1140px;overflow:hidden}

/* header */
.site-header{position:absolute;top:32px;left:95px;width:1012px;height:46px;z-index:5}
.brand{position:absolute;left:0;top:0;height:46px;display:flex;align-items:center;gap:10px}
.brand-mark{width:46px;height:46px;border-radius:50%;background:var(--violet-soft)}
.brand-name{font-weight:700;font-size:19px;line-height:1;white-space:nowrap}
.main-nav{position:absolute;left:238px;top:0;height:46px;display:flex;align-items:center;gap:25px;font-family:"Poppins",sans-serif;font-size:10px;font-weight:600;white-space:nowrap}
.main-nav a{color:var(--white);text-decoration:none}
.header-tools{position:absolute;right:0;top:0;height:46px;display:flex;align-items:center;gap:12px}
.theme-toggle{width:60px;height:32px;border-radius:16px;background:var(--white);display:flex;align-items:center;justify-content:space-around;padding:0 5px}
.theme-toggle .moon{width:24px;height:24px;border-radius:50%;background:var(--bg-deep);display:flex;align-items:center;justify-content:center}
.lang-btn{width:76px;height:32px;border-radius:16px;background:var(--white);color:var(--bg-deep);display:flex;align-items:center;justify-content:center;gap:6px;font-family:"Poppins",sans-serif;font-size:10px;font-weight:600}
.lang-dot{width:16px;height:16px;border-radius:50%;background:#2b3a8c}
.btn{display:flex;align-items:center;justify-content:space-between;border-radius:24px;background:linear-gradient(90deg,var(--btn-start),var(--btn-end));color:var(--white);font-family:"Poppins",sans-serif;font-weight:600;font-size:11px;text-decoration:none;padding:0 6px 0 22px;white-space:nowrap}
.btn .arrow{width:30px;height:30px;border-radius:50%;background:var(--white);display:flex;align-items:center;justify-content:center}
.btn-presale{width:150px;height:42px}

/* language dropdown */
.lang-menu{position:absolute;left:813px;top:96px;width:133px;background:var(--white);border-radius:8px;padding:12px 10px 10px;color:var(--bg-deep);font-family:"Poppins",sans-serif;font-size:11px;font-weight:600;z-index:10;box-shadow:0 8px 24px rgba(0,0,0,.3)}
.lang-menu::before{content:"";position:absolute;right:14px;top:-12px;border:12px solid transparent;border-bottom-color:var(--white);border-top:0}
.lang-menu li{list-style:none;display:flex;align-items:center;gap:14px;height:30px;border-bottom:1px solid #e6e0ee}
.lang-menu li:last-child{border-bottom:0}
.lang-menu .dot{width:20px;height:20px;border-radius:50%}

/* hero */
.orb-left{position:absolute;left:-120px;top:270px;width:185px;height:185px;border-radius:50%;background:linear-gradient(135deg,#3b1658,#24103f)}
.hero-title{position:absolute;left:96px;top:148px;font-size:68px;font-weight:600;line-height:67px;letter-spacing:-.5px}
.hero-sub{position:absolute;left:98px;top:370px;width:420px;font-family:"Poppins",sans-serif;font-size:14px;line-height:22px;color:var(--muted)}
.countdown{position:absolute;left:95px;top:445px;display:flex;align-items:center}
.count-box{width:85px;height:88px;border-radius:12px;background:rgba(255,255,255,.05);border:1px solid var(--line);text-align:center;padding-top:14px}
.count-label{font-family:"Poppins",sans-serif;font-size:13px;font-weight:500}
.count-num{font-size:36px;font-weight:600;color:var(--num);line-height:44px}
.count-sep{width:38px;text-align:center;font-size:26px;font-weight:700}
.btn-hero{position:absolute;left:97px;top:581px;width:174px;height:40px;font-size:10.5px;padding-left:18px}
.hero-art{position:absolute;left:615px;top:178px;width:450px;height:530px;border-radius:225px 225px 40px 40px;background:radial-gradient(circle at 45% 35%,#e3a24a 0%,#a05bbf 45%,#4b2f8f 75%,#2d8b58 100%);opacity:.85;z-index:1}

/* community card */
.community{position:absolute;left:95px;top:708px;width:1010px;height:480px;border-radius:60px;background:linear-gradient(180deg,#1d0b36,#150828);border:1px solid var(--line);z-index:2}
.community h2{position:absolute;top:86px;width:100%;text-align:center;font-size:37px;font-weight:600}
.feature{position:absolute;top:186px}
.feature p{margin-top:24px;font-size:21px;line-height:29px;font-weight:400;white-space:nowrap}
.feature-icons{display:flex;gap:9px}
.icon-tile{width:40px;height:40px;border-radius:8px;background:var(--violet-soft);display:flex;align-items:center;justify-content:center}
.icon-round{border-radius:50%}
.orb-ball{position:absolute;left:355px;top:652px;width:115px;height:115px;border-radius:50%;background:radial-gradient(circle at 35% 25%,#9a5ce0,#4a2385 45%,#1b0c33 75%);z-index:3}
.coins-art{position:absolute;left:865px;top:1088px;width:150px;height:80px;border-radius:40px;background:linear-gradient(135deg,#f2c14e,#c98a1c);z-index:3}
</style>
</head>
<body>
<div class="page">

  <header class="site-header">
    <div class="brand">
      <span class="brand-mark"></span>
      <span class="brand-name">TapDelver Rex</span>
    </div>
    <nav class="main-nav">
      <a href="#">HOME</a><a href="#">TOKENOMICS</a><a href="#">ROADMAP</a><a href="#">AIRDROP</a><a href="#">APP</a><a href="#">TEAM</a><a href="#">CONTACT</a>
    </nav>
    <div class="header-tools">
      <div class="theme-toggle">
        <span class="moon"><svg width="12" height="12" viewBox="0 0 24 24"><path d="M20 14A8 8 0 1 1 10 4a7 7 0 0 0 10 10z" fill="#fff"/></svg></span>
        <svg width="14" height="14" viewBox="0 0 24 24" fill="none" stroke="#13072a" stroke-width="2"><circle cx="12" cy="12" r="4"/><path d="M12 2v3M12 19v3M2 12h3M19 12h3M5 5l2 2M17 17l2 2M5 19l2-2M17 7l2-2"/></svg>
      </div>
      <div class="lang-btn"><span class="lang-dot"></span>ENG
        <svg width="8" height="6" viewBox="0 0 8 6"><path d="M1 1l3 3 3-3" stroke="#13072a" stroke-width="1.5" fill="none"/></svg></div>
      <a class="btn btn-presale" href="#">JOIN PRESALE
        <span class="arrow"><svg width="10" height="10" viewBox="0 0 10 10"><path d="M2 8L8 2M3 2h5v5" stroke="#13072a" stroke-width="1.4" fill="none"/></svg></span></a>
    </div>
  </header>

  <ul class="lang-menu">
    <li><span class="dot" style="background:#222"></span>German</li>
    <li><span class="dot" style="background:#e0a21c"></span>Spanish</li>
    <li><span class="dot" style="background:#2f55b5"></span>French</li>
    <li><span class="dot" style="background:#d0d6e6"></span>Russian</li>
    <li><span class="dot" style="background:#d63a2f"></span>Chinese</li>
    <li><span class="dot" style="background:#e23b2c"></span>Vietnamese</li>
    <li><span class="dot" style="background:#3658a8"></span>Slovak</li>
  </ul>

  <div class="orb-left"></div>

  <h1 class="hero-title">Mine Crypto.<br>Anywhere.<br>Anytime.</h1>
  <p class="hero-sub">Join the first meme-powered mobile mining revolution – no rigs, no nonsense, just your phone.</p>

  <div class="countdown">
    <div class="count-box"><div class="count-label">Days</div><div class="count-num">15</div></div>
    <div class="count-sep">:</div>
    <div class="count-box"><div class="count-label">Hours</div><div class="count-num">30</div></div>
    <div class="count-sep">:</div>
    <div class="count-box"><div class="count-label">Minutes</div><div class="count-num">60</div></div>
    <div class="count-sep">:</div>
    <div class="count-box"><div class="count-label">Seconds</div><div class="count-num">53</div></div>
  </div>

  <a class="btn btn-hero" href="#">JOIN PRESALE NOW
    <span class="arrow"><svg width="10" height="10" viewBox="0 0 10 10"><path d="M2 8L8 2M3 2h5v5" stroke="#13072a" stroke-width="1.4" fill="none"/></svg></span></a>

  <div class="hero-art" role="img" aria-label="Cartoon miner mascot with hard hat and pickaxe holding a phone, surrounded by gold TVDR coins, standing on a globe"></div>

  <section class="community">
    <h2>TVDR Community is Growing Fast</h2>
    <div class="feature" style="left:104px">
      <div class="feature-icons"><span class="icon-tile icon-round"></span></div>
      <p>Become part of the<br>fastest-growing Veltora<br>meme-mining community.</p>
    </div>
    <div class="feature" style="left:436px">
      <div class="feature-icons"><span class="icon-tile" style="background:none">
        <svg width="40" height="36" viewBox="0 0 40 36" fill="#8869af"><circle cx="20" cy="9" r="6"/><circle cx="8" cy="12" r="4.5"/><circle cx="32" cy="12" r="4.5"/><path d="M10 34c0-8 4-14 10-14s10 6 10 14z"/><path d="M1 32c0-6 3-11 7-11 2 0 3 1 4 2-2 3-3 6-3 9z"/><path d="M39 32c0-6-3-11-7-11-2 0-3 1-4 2 2 3 3 6 3 9z"/></svg>
      </span></div>
      <p>Thousands of early<br>supporters have<br>already joined.</p>
    </div>
    <div class="feature" style="left:685px">
      <div class="feature-icons"><span class="icon-tile"></span><span class="icon-tile"></span></div>
      <p>Join our Chatwire<br>&amp; Q (Blurbly) and don't<br>miss the presale.</p>
    </div>
  </section>

  <div class="orb-ball"></div>
  <div class="coins-art" role="img" aria-label="Stack of gold TVDR coins"></div>

</div>
</body>
</html>
```